Simple website design to introduce our software product.

Hello there! If you please, we want a lot of images (attached) to have this site to have our prospects thinking about how great it will be to use this product in their facility/clinic/office. There are a lot of happy people in the images attached and this is the feeling we want to convey...with a modern technology edge since our product digitizes the patient survey process and is used on a tablet PC.

We are finalizing a name change of our product, it is currently called "QVTR" but we are considering coming up with a better name so in the interim we will use QVTR as a place holder. The website domain where this site will reside is www.thepollharbor.com

1. We would like large scrolling images SIMILAR TO the top portion of this website : http://brightlanestudio.example/
Here are the verbiage blurbs to accompany the scrolling images:
Welcome to the next generation of Patient Experience Data Collection and Reporting. Presenting QVTR.

QVTR captures patient, nurse, doctor, employee and visitor satisfaction information in real time quickly and easily on a tablet PC.

QVTR gives you instantaneous benchmarking and reporting data including comparison reports, return rates, percentile rankings, positive and negative trending and much more.

QVTR DRAMATICALLY increases survey return rates.

QVTR empowers you to improve patient care when the data is relevant: NOW.

2. Please add something like the attached form called "QVTR info for pricing form" that says, "You won't believe our pricing! Click here" that includes the required fields as in the attached example.

3. We also want to highlight our Eco Trade Accreditation so please include the verbiage (from our company website): https://www.qvtrcorp.example/green.cfm I can provide you with the script to add the seal at the bottom left of the page.

4. We will provide verbiage for the About Us page and the Contact Us page

5. We would like to embed a video into the site and I can email you that code.

6. Please add the attached PLATINUM Eco Trade Accreditation logo on all pages and link it to this: http://www.etx.example/members/showseal/QkR4Nw==/WmVwaHlyVg==/

Looking forward to seeing what you present! Thank you for your entries. : )

We are very happy after seeing your designs.  Thank you so much.  Our product will be named The Poll Harbor, please update any and all instances of "QVTR" accordingly.  

Please be creative about this - How can an image of the tablet pc be used to navigate the site or maybe a specific section of the site?  

We have the domain www.thepollharbor.com and it is currently on a Weebly platform.  Could you/your team also launch our design on Weebly/Wordpress for us?

Hello!  Please be sure that the verbiage on your page designs is NOT pulled from our company website, QVTRience (qvtrcorp.example).  This is our PRODUCT website, not our COMPANY website.

Please make the site design concise.  Please include the following elements:  

1.  All designs must have a box (similar to file number 10 that is attached to the brief)
The title of the box needs to be "You won't believe our pricing!"
and has the following required fields:

*first name
*last name
*email
*phone
*company 
The submit button should say "GET IT!"  The position of this box should be on the right side of the page and while we want site visitors to see this box, we don't want it to be the first thing that draws their eye.  In other words, place this box softly/subtly on the site.  

2.  We like the images of the tablet pc.  It is very important that the site include pictures of PATIENTS with the tablet pc in their hands.  For this software, images of patients holding the tablet are more in alignment with the image we're trying to brand than are images of doctors/nurses holding the tablet pc. 

3.  Please update all designs to have the lead header/verbiage say "Welcome to the next generation of Patient Experience Data Collection and Reporting.  Presenting The Poll Harbor."  

4.  Please add this to the design too (if it's not already in your design), "Collect patient, doctor, nurse, employee and visitor Satisfaction/Experience feedback quickly, easily and in REAL TIME on a tablet pc."   

Please include this verbiage on the website - Users of The Poll Harbor consistently enjoy a survey return rate ABOVE 90%!

Target Market(s)

Healthcare facilities/hospitals/clinics/doctor's offices (initially, but the product can be customized for any industry).

Industry/Entity Type

Software

```html
<!DOCTYPE html>
<html lang="en">
<head>
<meta charset="utf-8">
<title>The Poll Harbor</title>
<link rel="stylesheet" href="https://fonts.googleapis.com/css2?family=Didact+Gothic&family=Noto+Sans:ital,wght@0,400;0,700;1,700&family=Arimo&display=swap">
<style>
  :root {
    --brand-red: #e03a16;
    --ink: #1c1c1c;
    --body-text: #4a4a4a;
    --nav-text: #333333;
    --field-border: #b9b9b9;
    --cta-green: #3db55a;
    --badge-green: #6cb52e;
    --dot: #6d7378;
  }
  * { box-sizing: border-box; margin: 0; padding: 0; }
  html, body { width: 880px; height: 1200px; overflow: hidden; background: #ffffff; }
  body { position: relative; font-family: "Noto Sans", sans-serif; color: var(--body-text); }

  .site-header { position: absolute; left: 80px; top: 22px; width: 720px; height: 40px; }
  .wordmark { position: absolute; left: 0; top: 0; display: flex; align-items: center; gap: 6px;
    font-family: "Didact Gothic", sans-serif; font-size: 29px; color: var(--ink); letter-spacing: -0.5px; }
  .wordmark-mark { width: 16px; height: 16px; background: var(--brand-red); }
  .main-nav { position: absolute; right: 0; top: 11px; display: flex; gap: 32px; font-size: 11.5px; color: var(--nav-text); }
  .main-nav .is-current { color: var(--brand-red); font-weight: 700; }

  .hero { position: absolute; left: 80px; top: 80px; width: 720px; height: 320px; overflow: hidden;
    background: linear-gradient(90deg, #98a4b0 0%, #c6ced6 40%, #e6e3e0 60%, #b9c2cb 100%); }
  .hero-photo { position: absolute; inset: 0; }
  .hero-band { position: absolute; left: 20px; right: 70px; top: 81px; height: 97px;
    background: linear-gradient(90deg, rgba(224,58,22,0) 0%, rgba(224,58,22,0.55) 25%, rgba(224,58,22,0.6) 50%, rgba(224,58,22,0.55) 75%, rgba(224,58,22,0) 100%); }
  .hero-caption { position: absolute; left: 0; right: 0; top: 90px; text-align: center;
    font-size: 30px; line-height: 39px; color: #ffffff; text-shadow: 0 1px 2px rgba(60,40,80,0.6); }
  .slider-dots { position: absolute; right: 24px; top: 21px; display: flex; gap: 7px; }
  .slider-dots span { width: 13px; height: 13px; background: var(--dot); }
  .slider-dots span.is-active { background: #9aa0a5; border: 1px solid #6d7378; }

  .content { position: absolute; left: 80px; top: 420px; width: 440px; }
  .content h2 { font-family: "Didact Gothic", sans-serif; font-weight: 400; font-size: 18.5px; line-height: 26px; color: var(--brand-red); margin-bottom: 7px; }
  .content p { font-size: 11px; line-height: 16.8px; margin-bottom: 16.8px; }
  .content h2.second-heading { margin-top: 26px; }

  .video { position: relative; width: 326px; height: 183px; margin: 3px 0 0 47px;
    background: linear-gradient(90deg, #000000 0%, #050a0d 30%, #0b3a58 60%, #0a78b0 85%, #0690c4 100%); }
  .video-controls { position: absolute; left: 8px; bottom: 8px; right: 8px; height: 31px; display: flex; gap: 7px; }
  .play-btn { width: 52px; height: 31px; background: rgba(20,20,20,0.9); border-radius: 3px; display: flex; align-items: center; justify-content: center; }
  .play-track { position: relative; flex: 1; background: rgba(20,20,20,0.85); border-radius: 3px; display: flex; align-items: center; padding: 0 8px; gap: 7px; }
  .timecode { position: absolute; left: -8px; top: -9px; background: #fff; color: #111; font-size: 8.5px; padding: 0 3px; font-family: "Arimo", sans-serif; }
  .progress { width: 98px; height: 8px; border: 1px solid #888; }
  .volume { display: flex; gap: 1.5px; }
  .volume span { width: 2px; height: 9px; background: #e0303a; }
  .hd { font-family: "Arimo", sans-serif; font-weight: 700; font-size: 13px; color: #666; }
  .player-name { font-family: "Arimo", sans-serif; font-size: 13px; color: #ffffff; }

  .pricing { position: absolute; left: 552px; top: 426px; width: 248px; height: 471px; background: var(--brand-red); }
  .pricing-title { height: 52px; padding-top: 17px; text-align: center; color: #fff; font-size: 14.5px; font-weight: 400; }
  .pricing-form { position: absolute; left: 10px; top: 52px; width: 230px; height: 410px; background: #fff; padding: 14px 21px 0 21px; font-family: "Arimo", sans-serif; }
  .field { margin-bottom: 13px; }
  .field label { display: block; font-size: 10px; color: #333; margin-bottom: 5px; }
  .field input { display: block; width: 189px; height: 29px; border: 1px solid var(--field-border); border-radius: 2px; background: #fff; }
  .submit { display: block; width: 189px; height: 35px; margin-top: 1px; border: 0; border-radius: 3px; background: var(--cta-green);
    color: #fff; font-family: "Noto Sans", sans-serif; font-style: italic; font-weight: 700; font-size: 18px; }

  .member-seal { position: absolute; left: 586px; top: 918px; width: 170px; height: 104px; border-radius: 10px; background: var(--badge-green); }
</style>
</head>
<body>
  <header class="site-header">
    <div class="wordmark">The Poll Harbor <span class="wordmark-mark"></span></div>
    <nav class="main-nav"><span class="is-current">Home</span><span>Contact Us</span></nav>
  </header>

  <section class="hero">
    <div class="hero-photo" role="img" aria-label="Smiling clinician holding a tablet showing the product screen"></div>
    <div class="hero-band"></div>
    <p class="hero-caption">QVTR empowers you to improve<br>patient care when the data is relevant</p>
    <div class="slider-dots"><span class="is-active"></span><span></span><span></span><span></span><span></span></div>
  </section>

  <main class="content">
    <h2>This a content heading</h2>
    <p>Lorem ipsum dolor sit amet, est altera aeterno ad, unum eruditi cu vis. Fierent eloquentiam neglegentur vel ea. Graecis fierent his cu. Per tritani invidunt eu, purto timeam voluptua vel ei, id vidisse efficiendi dissentiet pri. Ad iudicabit temporibus ius. Ex sea nullam dignissim.</p>
    <p>Ridens ancillae per ne, commodo disputando adversarium ex eos. Eu utinam veritus civibus per. Ferri congue audiam eum an, te vix zril soluta labore. Dicam voluptaria ut vis.</p>
    <p>Et ignota maiestatis efficiantur mei. Malis commune suavitate vix eu, ad aperiam philosophia quo. Lobortis necessitatibus mel cu, nonumy debitis et vel. Meis vivendum necessitatibus et sit. At per odio efficiendi. Id novum laoreet sea, mel ad quis propriae referrentur.</p>

    <div class="video" role="img" aria-label="Product introduction video">
      <div class="video-controls">
        <div class="play-btn"><svg width="14" height="16" viewBox="0 0 14 16"><path d="M0 0 L14 8 L0 16 Z" fill="#fff"/></svg></div>
        <div class="play-track">
          <span class="timecode">05:48</span>
          <div class="progress"></div>
          <div class="volume"><span></span><span></span><span></span><span></span><span></span><span></span><span></span><span></span></div>
          <span class="hd">HD</span>
          <svg width="11" height="11" viewBox="0 0 11 11" fill="#fff"><path d="M0 0h4L0 4zM11 0v4L7 0zM0 11V7l4 4zM11 11H7l4-4z"/></svg>
          <span class="player-name">clipreel</span>
        </div>
      </div>
    </div>

    <h2 class="second-heading">And another content heading</h2>
    <p>Lorem ipsum dolor sit amet, est altera aeterno ad, unum eruditi cu vis. Fierent eloquentiam neglegentur vel ea. Graecis fierent his cu. Per tritani invidunt eu, purto timeam voluptua vel ei, id vidisse efficiendi dissentiet pri. Ad iudicabit temporibus ius. Ex sea nullam dignissim.</p>
    <p>Ridens ancillae per ne, commodo disputando adversarium ex eos. Eu utinam veritus civibus per. Ferri congue audiam eum an, te vix zril soluta labore. Dicam voluptaria ut vis.</p>
    <p>Et ignota maiestatis efficiantur mei. Malis commune suavitate vix eu, ad aperiam philosophia quo. Lobortis necessitatibus mel cu, nonumy debitis et vel. Meis vivendum necessitatibus et sit. At per odio efficiendi. Id novum laoreet sea, mel ad quis propriae referrentur.</p>
  </main>

  <aside class="pricing">
    <h3 class="pricing-title">You won't believe our pricing!</h3>
    <form class="pricing-form">
      <div class="field"><label>First Name: *</label><input type="text"></div>
      <div class="field"><label>Last Name: *</label><input type="text"></div>
      <div class="field"><label>Email Address: *</label><input type="text"></div>
      <div class="field"><label>Phone Number: *</label><input type="text"></div>
      <div class="field"><label>Company Name: *</label><input type="text"></div>
      <div class="field"><label>Where did you hear about us?</label><input type="text"></div>
      <button type="button" class="submit">Get Started!</button>
    </form>
  </aside>

  <div class="member-seal" role="img" aria-label="Accreditation member seal"></div>
</body>
</html>
```